Quiet Harbor (title of music CD cover)

Create a CD jacket (front and back). Front artwork will be used on CD itself.The CD is an EP (6 songs). They are all love songs (Ballads). Violin, cello, piano, percussion, acoustic guitar, that sort of sound. I am looking for a sophisticated look to the CD. The title is Quiet Harbor and the subtitle is The Shape of Days. The picture is of me; Al Wren. I want this CD jacket to exude class. I have uploaded an example of what i think i want. Obviously rough on my part.

Besides the attached picture of me, I am looking for: my name, name of Cd (Quiet Harbor) and subtitle (The Shape of Days)
on front of CD

Back:
1. I Hear Your Heart Again (Al Wren) 3:26
2. All Tomorrow (Al Wren) 3:20
3. Through the Rain (Al Wren) 4:00
4. The Lantern (Al Wren) 3:53
5. Say Yes & Stay (Al Wren) 3:27
6. Quiet Harbor (Al Wren / Dale Pimmen) 4:28
Producer: Dale Pimmen
© 2017 Blue Lark Ventures, LLC

I have some more to go on back: barcode, publishing, additional credits
Updates

Target Market(s)

Adults 25-55

Industry/Entity Type

Music Download

Colors

Designer to choose colors to be used in the design.

Requirements
Must have
• Pic of me on front with title, subtitle and my name

```html
<!DOCTYPE html>
<html lang="en">
<head>
<meta charset="utf-8">
<title>Quiet Harbor – Al Wren – CD Jacket</title>
<link rel="stylesheet" href="https://fonts.googleapis.com/css2?family=Abril+Fatface&family=Crimson+Text:ital,wght@0,400;1,400&display=swap">
<style>
  :root {
    --ink: #07070c;
    --navy: #12152b;
    --navy-deep: #0a0b16;
    --gold-light: #f6a942;
    --gold-dark: #c8701c;
    --paper: #f4f1ea;
    --portrait-light: #8d8d8d;
    --portrait-mid: #3b3b3b;
  }
  * { margin: 0; padding: 0; box-sizing: border-box; }
  html, body {
    width: 1200px;
    height: 600px;
    overflow: hidden;
    background: var(--ink);
  }
  .jacket {
    position: relative;
    width: 1200px;
    height: 600px;
    overflow: hidden;
    font-family: "Crimson Text", Georgia, serif;
    color: var(--paper);
  }
  .leaf-field {
    position: absolute;
    inset: 0;
    background: radial-gradient(ellipse at 25% 50%, var(--navy) 0%, var(--navy-deep) 70%, var(--ink) 100%);
  }
  .portrait {
    position: absolute;
    left: 500px;
    top: 0;
    width: 430px;
    height: 600px;
    background:
      radial-gradient(ellipse 55% 45% at 45% 40%, var(--portrait-light) 0%, var(--portrait-mid) 55%, rgba(7,7,12,0) 100%),
      linear-gradient(90deg, rgba(7,7,12,0) 0%, rgba(7,7,12,0.9) 100%);
  }
  .gold-title {
    font-family: "Abril Fatface", "Playfair Display", serif;
    line-height: 0.95;
    background: linear-gradient(180deg, var(--gold-light) 0%, var(--gold-dark) 100%);
    -webkit-background-clip: text;
    background-clip: text;
    color: transparent;
  }
  .back {
    position: absolute;
    left: 70px;
    top: 74px;
  }
  .back .gold-title {
    font-size: 43px;
  }
  .track-list {
    list-style: none;
    margin-top: 34px;
    font-size: 18px;
    line-height: 27.6px;
  }
  .credits {
    margin-top: 30px;
    font-size: 18px;
    line-height: 25px;
  }
  .front {
    position: absolute;
    left: 890px;
    top: 78px;
  }
  .front .gold-title {
    font-size: 72px;
  }
  .subtitle {
    margin-top: 12px;
    margin-left: 4px;
    font-style: italic;
    font-size: 25px;
  }
  .artist {
    position: absolute;
    left: 912px;
    top: 428px;
    font-size: 58px;
    line-height: 1;
  }
</style>
</head>
<body>
  <div class="jacket">
    <div class="leaf-field" role="img" aria-label="Dark navy background with a repeating leafy vine pattern"></div>
    <div class="portrait" role="img" aria-label="Black and white portrait of the artist Al Wren"></div>

    <section class="back">
      <h2 class="gold-title">Quiet<br>Harbor</h2>
      <ol class="track-list">
        <li>1. I Hear Your Heart Again (Al Wren) 3:26</li>
        <li>2. All Tomorrow (Al Wren) 3:20</li>
        <li>3. Through the Rain (Al Wren) 4:00</li>
        <li>4. The Lantern (Al Wren) 3:53</li>
        <li>5. Say Yes &amp; Stay (Al Wren) 3:27</li>
        <li>6. Quiet Harbor (Al Wren / Dale Pimmen) 4:28</li>
      </ol>
      <p class="credits">Producer: Dale Pimmen<br>© 2017 Blue Lark Ventures, LLC</p>
    </section>

    <section class="front">
      <h1 class="gold-title">Quiet<br>Harbor</h1>
      <p class="subtitle">The Shape of Days</p>
    </section>
    <p class="artist">Al Wren</p>
  </div>
</body>
</html>
```